Powerpoint for consulting dentalpractices on management, improvement, and benchmarks

Fase 1: create 8-15 slides to be used for the model. The are the basic slideexamples for future presentation.
colour scheme and font types as in attachment for older powerpoint. Fonts, logo and colourscheme stay the same. Newer slidedeck contains newer ideas for new presentations. Smaller logo maybe better to be used for all slides. Normal logo for starting and end slide. Open for your inspiration and new suggestions
Fase 2 create slidemaster to enable us to create new slidedesks faster.

Target Market(s)

Dentalpractices (no dental images in powerpoint)

Industry/Entity Type

Dental practices

Font styles to use
Other font styles liked:
• Roobert for heading Normal Text Inter

Requirements
Must have
• Different slidemaster basic slides to quickly create slides with full slide pictures which still have a Molvaro touch. Content slides, slides with bullets and slides to show 3 -5 subjects
Nice to have
• New styling element for recognition of brand
Should not have
• round edges, complex slide master

```html
<!DOCTYPE html>
<html lang="en">
<head>
<meta charset="utf-8">
<title>Molvaro PPT</title>
<link href="https://fonts.googleapis.com/css2?family=Figtree:wght@400;500;600;800&family=Inter:wght@400;500;600;700&display=swap" rel="stylesheet">
<style>
:root{
  --green:#72bf4a;
  --blue:#0052a0;
  --stage:#c9c9c9;
  --ink:#1d1d1f;
  --muted:#6b6f76;
  --line:#cfd3d8;
  --soft:#f1f2f4;
}
*{margin:0;padding:0;box-sizing:border-box}
html,body{width:686px;height:1200px;overflow:hidden;background:var(--stage)}
body{position:relative;font-family:"Inter",sans-serif;color:var(--ink)}
.banner{position:absolute;left:0;top:0;width:686px;height:109px;background:var(--green);display:flex;align-items:center;justify-content:center}
.banner h1{font-family:"Figtree",sans-serif;font-weight:800;font-size:37px;color:#fff;letter-spacing:.5px}
.slide{position:absolute;width:302px;height:170px;background:#fff;overflow:hidden}
.s1{left:30px;top:173px}.s2{left:354px;top:173px}
.s3{left:30px;top:372px}.s4{left:354px;top:372px}
.s5{left:30px;top:570px}.s6{left:354px;top:570px}
.s7{left:30px;top:768px}.s8{left:354px;top:768px}
.s9{left:192px;top:966px}
.abs{position:absolute}
.photo{position:absolute}
.wordmark{position:absolute;font-family:"Figtree",sans-serif;font-weight:600;color:var(--blue);letter-spacing:-.2px}
.mini-mark{position:absolute;right:12px;top:11px;font-family:"Figtree",sans-serif;font-weight:600;font-size:5.5px;color:var(--green)}
.title{position:absolute;left:17px;top:12px;font-family:"Figtree",sans-serif;font-weight:500;font-size:10px;color:var(--ink)}
.title::after{content:"";position:absolute;left:0;bottom:-3px;width:40px;height:1px;background:var(--blue)}
.footer{position:absolute;right:0;bottom:6px;display:flex;align-items:center;gap:4px}
.footer span{font-size:3px;color:var(--muted)}
.footer b{display:block;width:10px;height:6px;background:var(--green);color:#fff;font-size:3px;font-weight:500;text-align:center;line-height:6px}
.tiny{font-size:4px;line-height:1.3}
ul.bul{list-style:none}
ul.bul li{position:relative;padding-left:4px;font-size:3.4px;line-height:1.35;color:var(--muted);margin-bottom:2px}
ul.bul li::before{content:"";position:absolute;left:0;top:1.7px;width:1.2px;height:1.2px;border-radius:50%;background:currentColor}
/* slide 2 */
.toc-card{position:absolute;width:82px;height:29px;background:#fff;border:.6px solid var(--line);padding:6px 6px 0}
.toc-card h4{font-size:4px;font-weight:500;margin-bottom:3px}
.toc-card p{font-size:3px;line-height:1.3;color:var(--muted)}
.num{position:absolute;width:11px;height:11px;border-radius:50%;background:var(--green);color:#fff;font-size:4px;text-align:center;line-height:11px;top:-5px;right:-4px;border:.8px solid #fff}
/* slide 3 */
.col-head{position:absolute;display:flex;align-items:center;gap:5px;font-size:4.3px}
.col-head i{display:block;width:8px;height:7px;background:var(--blue)}
/* slide 5 */
.step{position:absolute;width:18px;height:18px;border-radius:50%;color:#fff;font-size:5.5px;text-align:center;line-height:18px}
.sub{position:absolute;font-size:4.6px;font-weight:500}
/* table */
.grid{position:absolute;left:17px;top:45px;width:268px;border-collapse:collapse;table-layout:fixed;font-size:3.5px}
.grid td,.grid th{height:10.4px;text-align:center;border-bottom:.5px solid #e3e5e8;font-weight:400}
.grid th{height:9.5px;background:var(--green);color:#fff;border-left:.5px solid #fff}
.grid td.no{background:#b9bcc0;color:#fff;border-bottom:.5px solid #fff}
.grid td.name{text-align:left;padding-left:4px}
.grid tr:nth-child(even) td:not(.no){background:#f4f5f6}
.grid .cap{background:var(--blue);height:10px;font-weight:600}
/* thank you */
.contact{position:absolute;left:17px;display:flex;align-items:center;gap:6px;color:#fff;font-size:5.6px;line-height:1.2}
.contact .ic{width:16px;height:16px;border-radius:50%;background:#fff;display:flex;align-items:center;justify-content:center;flex:none}
</style>
</head>
<body>

<header class="banner"><h1>MOLVARO PPT</h1></header>

<!-- 1 Cover -->
<section class="slide s1">
  <div class="photo" role="img" aria-label="Photo of hands forming a heart shape" style="left:120px;top:0;width:182px;height:140px;background:linear-gradient(100deg,#fff 0%,#f5ece6 35%,#e2c7b4 75%,#c99f85 100%)"></div>
  <svg class="abs" style="left:0;top:0" width="302" height="170" viewBox="0 0 302 170">
    <path d="M0 134 C60 160 170 165 302 95 L302 170 L0 170 Z" fill="var(--blue)"/>
    <path d="M0 134 C60 160 170 165 302 95 L302 101 C180 158 70 160 0 134 Z" fill="var(--green)"/>
  </svg>
  <div class="wordmark" style="left:16px;top:34px;font-size:14px">Molvaro</div>
  <div class="abs" style="left:17px;top:62px;width:140px;font-family:'Figtree',sans-serif;font-size:9.6px;line-height:1.25">Lorem ipsum dolor sit amet, consectetuer adipiscing elit.</div>
  <div class="abs" style="left:17px;top:94px;width:140px;font-size:4.2px;line-height:1.3;color:var(--muted)">Fusce posuere, magna sed pulvinar ultricies, purus lectus malesuada libero, sit amet commodo magna eros quis urna.</div>
</section>

<!-- 2 Table of content -->
<section class="slide s2">
  <div class="abs" style="left:0;top:136px;width:302px;height:34px;background:var(--blue)"></div>
  <div class="title">Table of content</div>
  <div class="mini-mark">Molvaro</div>
  <div class="toc-card" style="left:17px;top:42px"><span class="num">01</span><h4>What is lorem ipsum?</h4><p>Lorem Ipsum is simply dummy text of the printing and typesetting industry</p></div>
  <div class="toc-card" style="left:110px;top:42px"><span class="num">02</span><h4>What is lorem ipsum?</h4><p>Lorem Ipsum is simply dummy text of the printing and typesetting industry</p></div>
  <div class="toc-card" style="left:203px;top:42px"><span class="num">03</span><h4>What is lorem ipsum?</h4><p>Lorem Ipsum is simply dummy text of the printing and typesetting industry</p></div>
  <div class="toc-card" style="left:17px;top:82px"><span class="num">04</span><h4>What is lorem ipsum?</h4><p>Lorem Ipsum is simply dummy text of the printing and typesetting industry</p></div>
  <div class="toc-card" style="left:110px;top:82px"><span class="num">05</span><h4>What is lorem ipsum?</h4><p>Lorem Ipsum is simply dummy text of the printing and typesetting industry</p></div>
  <div class="toc-card" style="left:203px;top:82px"><span class="num">06</span><h4>What is lorem ipsum?</h4><p>Lorem Ipsum is simply dummy text of the printing and typesetting industry</p></div>
  <div class="toc-card" style="left:17px;top:121px"><span class="num">07</span><h4>What is lorem ipsum?</h4><p>Lorem Ipsum is simply dummy text of the printing and typesetting industry</p></div>
  <div class="toc-card" style="left:110px;top:121px"><span class="num">08</span><h4>What is lorem ipsum?</h4><p>Lorem Ipsum is simply dummy text of the printing and typesetting industry</p></div>
  <div class="toc-card" style="left:203px;top:121px"><span class="num">09</span><h4>What is lorem ipsum?</h4><p>Lorem Ipsum is simply dummy text of the printing and typesetting industry</p></div>
  <div class="footer" style="color:#fff"><span style="color:#dfe8f4">molvaro.nl</span><b>2</b></div>
</section>

<!-- 3 Three headings -->
<section class="slide s3">
  <div class="title">Your title slide goes here</div>
  <div class="mini-mark">Molvaro</div>
  <div class="abs" style="left:13px;top:37px;width:109px;height:55px;background:var(--green);color:#fff;font-size:4.2px;font-weight:700;line-height:1.25;padding:14px 6px 0 10px">Lorem Ipsum is simply dummy text of the printing and typesetting industry. Lorem Ipsum has been the industry's standard dummy text ever since the 1500s, when an unknown printer took a galley of type.</div>
  <div class="photo" role="img" aria-label="Photo of a microscope and gloved hands in a lab" style="left:122px;top:37px;width:168px;height:55px;background:linear-gradient(90deg,#9aa3ad 0%,#d9dde3 45%,#b9c9df 70%,#4f86c9 100%)"></div>
  <div class="col-head" style="left:23px;top:107px"><i></i>HEADING 1</div>
  <div class="col-head" style="left:111px;top:107px"><i></i>HEADING 2</div>
  <div class="col-head" style="left:199px;top:107px"><i style="border-radius:50%"></i>HEADING 2</div>
  <ul class="bul abs" style="left:24px;top:121px;width:80px"><li>Lorem ipsum is simply dummy text</li><li>Of the printing and typesetting industry.</li><li>Lorem ipsum has been</li><li>The industry's standard dummy text</li><li>Ever since the 1500s,</li></ul>
  <ul class="bul abs" style="left:112px;top:121px;width:80px"><li>Lorem ipsum is simply dummy text</li><li>Of the printing and typesetting industry.</li><li>Lorem ipsum has been</li><li>The industry's standard dummy text</li><li>Ever since the 1500s,</li></ul>
  <ul class="bul abs" style="left:200px;top:121px;width:80px"><li>Lorem ipsum is simply dummy text</li><li>Of the printing and typesetting industry.</li><li>Lorem ipsum has been</li><li>The industry's standard dummy text</li><li>Ever since the 1500s,</li></ul>
  <div class="footer"><span>molvaro.nl</span><b>3</b></div>
</section>

<!-- 4 Photo collage -->
<section class="slide s4">
  <svg class="abs" style="left:0;top:0" width="302" height="170"><polygon points="0,0 56,0 93,170 0,170" fill="var(--blue)"/></svg>
  <div class="abs" style="left:9px;top:156px;transform:rotate(-90deg);transform-origin:0 0;font-family:'Figtree',sans-serif;font-weight:600;font-size:14px;color:#3a74b5">Molvaro</div>
  <div class="photo" role="img" aria-label="Photo of a team at work in a practice" style="left:17px;top:21px;width:112px;height:73px;background:linear-gradient(120deg,#6f8fb8,#c8d3e0 60%,#eef0f3);border:1.5px solid #fff"></div>
  <div class="photo" role="img" aria-label="Photo of two colleagues reviewing a tablet" style="left:39px;top:76px;width:117px;height:76px;background:linear-gradient(120deg,#9a8e80,#cdc6bd 45%,#3c4656);border:2px solid #fff;box-shadow:0 1px 3px rgba(0,0,0,.25)"></div>
  <div class="mini-mark">Molvaro</div>
  <div class="abs" style="left:174px;top:43px;font-family:'Figtree',sans-serif;font-weight:500;font-size:10px;line-height:1.2">Your title slide<br>goes here</div>
  <div class="abs tiny" style="left:177px;top:78px;width:106px;font-size:3.9px">Lorem ipsum dolor sit amet, consectetur adipiscing elit, sed do eiusmod tempor incididunt ut labore et dolore magna aliqua. Ut enim ad minim veniam, quis nostrud exercitation ullamco laboris nisi ut aliquip ex ea commodo consequat. Duis aute irure dolor in reprehenderit in voluptate velit esse cillum dolore eu fugiat nulla pariatur.</div>
  <div class="abs tiny" style="left:177px;top:121px;width:106px;font-size:3.9px;color:var(--green)">Excepteur sint occaecat cupidatat non proident, sunt in culpa qui officia deserunt mollit anim id est laborum.</div>
  <div class="footer"><span>molvaro.nl</span><b>4</b></div>
</section>

<!-- 5 Two steps -->
<section class="slide s5">
  <div class="abs" style="left:115px;top:0;width:187px;height:170px;background:var(--soft)"></div>
  <div class="photo" role="img" aria-label="Photo of clinical equipment in a bright room" style="left:0;top:0;width:115px;height:170px;background:linear-gradient(160deg,#e9ecef 0%,#cfd5db 50%,#8f979f 100%)"></div>
  <div class="abs" style="left:61px;top:15px;width:212px;height:139px;background:#fff"></div>
  <div class="mini-mark">Molvaro</div>
  <div class="title" style="left:78px;top:27px">Your title slide goes here</div>
  <div class="step" style="left:79px;top:54px;background:var(--green)">01</div>
  <div class="step" style="left:177px;top:54px;background:var(--blue)">02</div>
  <div class="sub" style="left:78px;top:78px;color:var(--green)">Lorem ipsum dolor sit amet</div>
  <div class="sub" style="left:177px;top:78px;color:var(--blue)">Lorem ipsum dolor sit amet</div>
  <ul class="bul abs" style="left:79px;top:88px;width:80px"><li>Lorem ipsum dolor sit amet, consectetur adipiscing elit</li><li>Sed do eiusmod tempor incididunt ut labore et dolore magna aliqua.</li><li>Ut enim ad minim veniam, quis nostrud exercitation ullamco laboris nisi ut aliquip ex ea commodo consequat.</li></ul>
  <ul class="bul abs" style="left:178px;top:88px;width:80px"><li>Lorem ipsum dolor sit amet, consectetur adipiscing elit</li><li>Sed do eiusmod tempor incididunt ut labore et dolore magna aliqua.</li><li>Ut enim ad minim veniam</li><li>Quis nostrud exercitation ullamco laboris nisi ut aliquip ex ea commodo consequat.</li></ul>
  <div class="footer"><span>molvaro.nl</span><b>6</b></div>
</section>

<!-- 6 Quadrants -->
<section class="slide s6">
  <div class="title">Your title slide goes here</div>
  <div class="mini-mark">Molvaro</div>
  <div class="abs" style="left:14px;top:40px;width:135px;height:56px;background:var(--green);color:#fff;padding:8px 9px 0">
    <div style="font-size:5px;font-weight:500;margin-bottom:4px">Lorem ipsum dolor sit amet</div>
    <ul class="bul"><li style="color:#fff">Lorem ipsum dolor sit amet, consectetur adipiscing elit, sed do eiusmod tempor incididunt ut labore et dolore magna aliqua.</li><li style="color:#fff">Ut enim ad minim veniam, quis nostrud exercitation ullamco laboris nisi ut aliquip ex ea commodo consequat.</li></ul>
  </div>
  <div class="photo" role="img" aria-label="Photo of professionals at work" style="left:153px;top:40px;width:135px;height:56px;background:linear-gradient(120deg,#5d7fae,#c7d2df 55%,#eef0f3)"></div>
  <div class="photo" role="img" aria-label="Photo of a microscope in a lab" style="left:14px;top:100px;width:135px;height:56px;background:linear-gradient(90deg,#e3e6ea,#9ea6ae 50%,#6d9ad2)"></div>
  <div class="abs" style="left:166px;top:100px;width:122px;height:56px;background:var(--blue);color:#fff;padding:7px 8px 0 10px">
    <div style="font-size:5px;font-weight:500;margin-bottom:4px">Lorem ipsum dolor sit amet</div>
    <ul class="bul"><li style="color:#fff">Lorem ipsum dolor sit amet, consectetur adipiscing elit, sed do eiusmod tempor incididunt ut labore et dolore magna aliqua.</li><li style="color:#fff">Ut enim ad minim veniam, quis nostrud exercitation ullamco laboris nisi ut aliquip ex ea commodo consequat.</li></ul>
  </div>
  <svg class="abs" style="left:131px;top:78px" width="40" height="40" viewBox="0 0 40 40">
    <circle cx="20" cy="20" r="19" fill="#fff"/>
    <circle cx="20" cy="20" r="16" fill="none" stroke="#d2d5d9" stroke-width=".8"/>
    <circle cx="20" cy="18" r="5" fill="none" stroke="#8b9096" stroke-width="1"/>
    <path d="M17.5 18l1.8 1.8 3.2-3.4" fill="none" stroke="#8b9096" stroke-width="1"/>
    <path d="M17.5 24h5M18 26h4" stroke="#8b9096" stroke-width="1"/>
  </svg>
  <div class="footer"><span>molvaro.nl</span><b>5</b></div>
</section>

<!-- 7 Full photo -->
<section class="slide s7">
  <div class="photo" role="img" aria-label="Photo of a smiling professional in a white coat in a bright room" style="left:7px;top:7px;width:288px;height:155px;background:linear-gradient(100deg,#e9ebee 0%,#f7f7f8 40%,#dfe3e7 100%)"></div>
  <div class="abs" style="left:0;top:94px;width:196px;height:51px;background:var(--green)"></div>
  <div class="abs" style="left:0;top:94px;width:191px;height:51px;background:var(--blue)"></div>
  <div class="abs" style="left:11px;top:116px;font-family:'Figtree',sans-serif;font-weight:600;font-size:7px;color:#fff">Molvaro</div>
  <div class="abs" style="left:52px;top:102px;width:.6px;height:34px;background:#fff"></div>
  <div class="abs" style="left:65px;top:103px;font-family:'Figtree',sans-serif;font-weight:500;font-size:9.4px;color:#fff">Your title slide goes here</div>
  <div class="abs" style="left:65px;top:118px;width:118px;font-size:4px;line-height:1.3;color:#fff">Lorem ipsum dolor sit amet, consectetur adipiscing elit, sed do eiusmod tempor incididunt ut labore et dolore magna aliqua.</div>
</section>

<!-- 8 Table -->
<section class="slide s8">
  <div class="title">Your title slide goes here</div>
  <div class="mini-mark">Molvaro</div>
  <div class="abs" style="left:13px;top:41px;width:276px;height:113px;background:#fff;box-shadow:0 0 4px rgba(0,0,0,.18)"></div>
  <table class="grid">
    <colgroup><col style="width:17px"><col style="width:63px"><col><col><col><col></colgroup>
    <tr><td style="border:0"></td><td style="border:0"></td><th class="cap" colspan="4">Lorem ipsum</th></tr>
    <tr><th style="background:#b9bcc0">No</th><th>Name</th><th>Title 1</th><th>Title 2</th><th>Title 3</th><th>Title 3</th></tr>
    <tr><td class="no">1</td><td class="name">Lorem ipsum</td><td>Lorem</td><td>Lorem</td><td>Lorem</td><td>Lorem</td></tr>
    <tr><td class="no">2</td><td class="name">Lorem ipsum</td><td>-</td><td>-</td><td>-</td><td>-</td></tr>
    <tr><td class="no">3</td><td class="name">Lorem ipsum</td><td>Lorem</td><td>Lorem</td><td>Lorem</td><td>Lorem</td></tr>
    <tr><td class="no">4</td><td class="name">Lorem ipsum</td><td>xxx</td><td>xxx</td><td>xxx</td><td>xxx</td></tr>
    <tr><td class="no">5</td><td class="name">Lorem ipsum</td><td>Lorem</td><td>Lorem</td><td>Lorem</td><td>Lorem</td></tr>
    <tr><td class="no">6</td><td class="name">Lorem ipsum</td><td>No</td><td>Yes</td><td>No</td><td>No</td></tr>
    <tr><td class="no">7</td><td class="name">Lorem ipsum</td><td>Lorem</td><td>Lorem</td><td>Lorem</td><td>Lorem</td></tr>
    <tr><td class="no">8</td><td class="name" style="border-bottom:.8px solid var(--blue)">Lorem ipsum</td><td style="border-bottom:.8px solid var(--blue)">Yes</td><td style="border-bottom:.8px solid var(--blue)">Yes</td><td style="border-bottom:.8px solid var(--blue)">Yes</td><td style="border-bottom:.8px solid var(--blue)">Yes</td></tr>
  </table>
  <div class="footer"><span>molvaro.nl</span><b>8</b></div>
</section>

<!-- 9 Thank you -->
<section class="slide s9">
  <div class="photo" role="img" aria-label="Photo of a researcher using a microscope" style="left:0;top:0;width:302px;height:170px;clip-path:polygon(133px 0,302px 0,302px 170px,100px 170px);background:linear-gradient(110deg,#eef1f5 0%,#9aa2ab 35%,#3b4047 55%,#a9bfdc 75%,#4d8ad0 100%)"></div>
  <svg class="abs" style="left:0;top:0" width="302" height="170">
    <polygon points="0,57 192,57 138,170 0,170" fill="var(--green)"/>
    <polyline points="186,63 135,170" fill="none" stroke="#fff" stroke-width=".6"/>
  </svg>
  <div class="wordmark" style="left:19px;top:30px;font-size:14px">Molvaro</div>
  <div class="abs" style="left:17px;top:76px;font-family:'Figtree',sans-serif;font-weight:500;font-size:13px;color:#fff">Thank you!</div>
  <div class="contact" style="top:96px">
    <span class="ic"><svg width="8" height="9" viewBox="0 0 8 9"><path d="M4 9S0.5 5.5 0.5 3.5a3.5 3.5 0 0 1 7 0C7.5 5.5 4 9 4 9z" fill="var(--green)"/><circle cx="4" cy="3.5" r="1.2" fill="#fff"/></svg></span>
    <span><b style="font-weight:600">Molvaro</b><br>Lindeweg 48<br>3512 KL Veldhoven</span>
  </div>
  <div class="contact" style="top:121px">
    <span class="ic"><svg width="9" height="7" viewBox="0 0 9 7"><rect width="9" height="7" fill="var(--green)"/><path d="M0 0l4.5 3.5L9 0" fill="none" stroke="#fff" stroke-width=".8"/></svg></span>
    <span>info@molvaro.nl</span>
  </div>
  <div class="contact" style="top:141px">
    <span class="ic"><svg width="9" height="9" viewBox="0 0 9 9"><circle cx="4.5" cy="4.5" r="4" fill="var(--green)"/><path d="M.5 4.5h8M4.5 .5c-2 2.5-2 5.5 0 8M4.5 .5c2 2.5 2 5.5 0 8" fill="none" stroke="#fff" stroke-width=".6"/></svg></span>
    <span>molvaro.nl</span>
  </div>
</section>

</body>
</html>
```